Take Out Menu

We are looking to redo our take out menu.
See current attached file for our current design.
The menu should make you hungry when looking at the pictures.
Target Market(s)
All of our customers.
Industry/Entity Type
Restaurant
Contact Information for Business Card
I will attach an image of our current card. It has the details of what we need on it.
Colors
Designer to choose colors to be used in the design.
Requirements
Must have
- A fresh look and feel. We must use our current logo branding. You can look at Velkoran on google to see what our restaurants look like.
Nice to have
- Easy read with food pictures.

```html
<!DOCTYPE html>
<html lang="en">
<head>
<meta charset="utf-8">
<title>Take Out Menu</title>
<link href="https://fonts.googleapis.com/css2?family=Alfa+Slab+One&family=Oswald:wght@500;600&family=Josefin+Sans:wght@600;700&display=swap" rel="stylesheet">
<style>
:root{
  --wood-light:#e6d2b5;
  --wood-mid:#d8bf9c;
  --parchment:#d9b684;
  --parchment-light:#e7cda0;
  --parchment-edge:#8a5a2b;
  --ink:#2e2118;
  --title:#4a2f22;
  --accent:#b3261e;
  --tomato:#d8321f;
  --greens:#3f6b25;
  --plate:#f3f1ec;
}
*{margin:0;padding:0;box-sizing:border-box}
html,body{width:1200px;height:848px;overflow:hidden;background:var(--wood-light)}
.menu{position:relative;width:1200px;height:848px;overflow:hidden;
  background:linear-gradient(90deg,var(--wood-light),var(--wood-mid) 50%,var(--wood-light));
  font-family:"Josefin Sans",sans-serif;color:var(--ink)}
.panel{position:absolute;border-radius:6px;
  background:radial-gradient(ellipse at center,var(--parchment-light) 40%,var(--parchment) 75%,var(--parchment-edge) 100%);
  box-shadow:2px 3px 6px rgba(60,35,15,.45)}
.tag{position:absolute;border-radius:5px;text-align:center;
  background:radial-gradient(ellipse at center,var(--parchment-light) 35%,var(--parchment) 70%,var(--parchment-edge) 100%);
  box-shadow:2px 3px 5px rgba(60,35,15,.4);display:flex;flex-direction:column;justify-content:center;
  font-weight:600;font-size:10.5px;line-height:1.05;color:var(--ink)}
.tag small{font-size:6.5px;display:block}
.tag .price{font-size:8px}
.photo{position:absolute}
.slab-title{position:absolute;font-family:"Alfa Slab One",serif;color:var(--title);text-align:center;line-height:.95}
.condensed-title{position:absolute;z-index:2;font-family:Oswald,sans-serif;font-weight:500;color:var(--accent);transform-origin:left top;line-height:1;white-space:nowrap}
.list{position:absolute}
.row{display:flex;align-items:baseline;font-weight:700;letter-spacing:.6px;white-space:nowrap}
.row .leader{flex:1;border-bottom:2px dotted var(--ink);margin:0 2px;transform:translateY(-3px)}
.note{font-weight:700;color:var(--accent);font-size:8.5px;letter-spacing:.3px;white-space:nowrap}
.sub{font-size:8px;display:block;margin-top:-2px}
.red{color:var(--accent)}
.portions-table{position:absolute;left:469px;top:366px;border-collapse:collapse;font-weight:600;font-size:11.3px;letter-spacing:.3px}
.portions-table td,.portions-table th{padding:0;height:14.2px;white-space:nowrap;font-weight:600;text-align:left}
.portions-table th{font-size:11px}
.portions-table .name{width:136px}
.portions-table .p{width:49px}
.choice{position:absolute;font-weight:700;font-size:14px;line-height:1;letter-spacing:.5px}
.choice .sub{font-size:8.5px;margin-top:0}
</style>
</head>
<body>
<main class="menu">

  <div class="photo" role="img" aria-label="Red bell pepper" style="left:338px;top:0;width:150px;height:84px;border-radius:40% 45% 50% 50%;background:radial-gradient(circle at 40% 40%,#f04a34,#c81a14 60%,#8e0c0a)"></div>

  <!-- Roti / Rice dishes -->
  <section class="panel" style="left:24px;top:32px;width:352px;height:324px"></section>
  <h2 class="condensed-title" style="left:70px;top:44px;font-size:60px;transform:scaleX(.6)">ROTI/RICE DISHES</h2>
  <div class="list" style="left:70px;top:112px;width:262px;font-size:14.5px;line-height:18.4px">
    <div class="row">BONE-IN CHICKEN<span class="leader"></span>$12.99</div>
    <div class="row">BONELESS CHICKEN<span class="leader"></span>$14.99</div>
    <div class="row">BONE-IN GOAT<span class="leader"></span>$13.99</div>
    <div class="row">BONELESS GOAT<span class="leader"></span>$15.99</div>
    <div class="row">SHRIMP<span class="leader"></span>$15.99</div>
    <div class="row">DUCK<span class="leader"></span>$15.99</div>
    <div class="row">STEW CHICKEN<span class="leader"></span>$12.49</div>
    <div class="row">PACHOUNI<span class="leader"></span>$14.99</div>
  </div>
  <p class="note" style="position:absolute;left:70px;top:265px">SERVED WITH CHOICE OF DHAL POTATO OR CHANNA</p>
  <div class="condensed-title" style="left:70px;top:274px;font-size:60px;transform:scaleX(.5)">VEGGIE</div>
  <div class="list" style="left:168px;top:282px;width:164px;font-size:14px;line-height:17px">
    <div class="row">VEGGIE <small style="font-size:9px">&nbsp;(4 ITEMS)</small><span class="leader"></span>$13.99</div>
    <div class="row">POTATO/</div>
    <div class="row">CHANNA<span class="leader"></span>$9.99</div>
  </div>

  <!-- Rice dishes -->
  <h2 class="slab-title" style="left:36px;top:398px;width:328px;font-size:38px;letter-spacing:2px">RICE DISHES</h2>
  <div class="tag" style="left:28px;top:456px;width:162px;height:48px">JERK CHICKEN<small>SERVED WITH RICE AND PEAS</small><span class="price">$13.49</span></div>
  <div class="tag" style="left:204px;top:456px;width:162px;height:48px">STEW CHICKEN<small>SERVED WITH CALALLO</small><span class="price">$12.99</span></div>
  <div class="photo" role="img" aria-label="Jerk chicken with rice, peas and salad on a white plate" style="left:36px;top:508px;width:152px;height:112px;background:radial-gradient(circle,#6b4526 25%,#8a6a3a 45%,var(--plate) 70%)"></div>
  <div class="photo" role="img" aria-label="Stew chicken with callaloo and salad on a white plate" style="left:210px;top:508px;width:152px;height:112px;background:radial-gradient(circle,#6a3a22 20%,#7d8a3a 45%,var(--plate) 70%)"></div>
  <div class="tag" style="left:30px;top:646px;width:162px;height:46px">CURRY KING FISH<span class="price">$15.99</span></div>
  <div class="tag" style="left:204px;top:646px;width:162px;height:48px">BAKE<small>WITH SMOKED HERRING AND SALTFISH</small><span class="price">$11.99</span></div>
  <div class="photo" role="img" aria-label="Curry king fish with salad on a white plate" style="left:32px;top:696px;width:154px;height:112px;background:radial-gradient(circle,#8c8a3a 22%,#9db56a 42%,var(--plate) 68%)"></div>
  <div class="tag" style="left:204px;top:704px;width:162px;height:48px">BAKE AND SHARK<span class="price">$12.99</span></div>
  <div class="photo" role="img" aria-label="Tomato" style="left:156px;top:812px;width:128px;height:60px;border-radius:50%;background:radial-gradient(circle at 45% 40%,#f25a3c,var(--tomato) 55%,#a0170e)"></div>
  <div class="photo" role="img" aria-label="Tomato" style="left:294px;top:752px;width:164px;height:130px;border-radius:50%;background:radial-gradient(circle at 45% 40%,#f25a3c,var(--tomato) 55%,#a0170e)"></div>

  <!-- Plain roti -->
  <section class="panel" style="left:440px;top:28px;width:316px;height:228px"></section>
  <h2 class="slab-title" style="left:440px;top:50px;width:316px;font-size:34px">PLAIN<br>ROTI</h2>
  <div class="list" style="left:470px;top:126px;width:254px;font-size:14.5px;line-height:18.5px">
    <div class="row">DHALPURIE<span class="leader"></span>$3.99</div>
    <div class="row">PARATHA<span class="leader"></span>$3.99</div>
    <div class="row">SADA<span class="leader"></span>$3.99</div>
    <div class="row">BAKE<span class="leader"></span>$3.99</div>
  </div>

  <!-- Portions -->
  <section class="panel" style="left:424px;top:296px;width:334px;height:268px"></section>
  <h2 class="slab-title" style="left:424px;top:326px;width:334px;font-size:36px">PORTIONS</h2>
  <table class="portions-table">
    <tr><th class="name"></th><th class="p">8oz</th><th class="p">16oz</th><th class="p">20oz</th></tr>
    <tr><td>BONE-IN CHICKEN</td><td>$6.99</td><td>$12.99</td><td>$15.99</td></tr>
    <tr><td>BONELESS CHICKEN</td><td>$10.49</td><td>$19.99</td><td>$23.99</td></tr>
    <tr><td>BONE-IN GOAT</td><td>$8.99</td><td>$16.99</td><td>$20.99</td></tr>
    <tr><td>BONELESS GOAT</td><td>$10.99</td><td>$20.99</td><td>$25.99</td></tr>
    <tr><td>BONELESS LAMB</td><td>$10.99</td><td>$20.99</td><td>$25.99</td></tr>
    <tr><td>SHRIMP</td><td>$12.99</td><td>$24.99</td><td>$29.99</td></tr>
    <tr><td>DUCK</td><td>$8.99</td><td>$17.99</td><td>$21.99</td></tr>
    <tr><td>PACHOUNI</td><td>$7.99</td><td>$14.99</td><td>$17.99</td></tr>
    <tr><td>POTATO</td><td>$4.99</td><td>$8.99</td><td>$10.99</td></tr>
    <tr><td>OTHER VEGGIE</td><td>$7.99</td><td>$14.99</td><td>$17.99</td></tr>
  </table>
  <div class="photo" role="img" aria-label="Plate of doubles, pholourie, aloo pie and dipping sauce" style="left:424px;top:530px;width:196px;height:110px;border-radius:50%;background:radial-gradient(ellipse,#d9a24e 30%,#e8c27a 55%,var(--plate) 72%,transparent 74%)"></div>

  <!-- Appetizers -->
  <section class="panel" style="left:440px;top:628px;width:316px;height:188px"></section>
  <h2 class="slab-title" style="left:440px;top:640px;width:316px;font-size:34px">APPETIZERS</h2>
  <div class="list" style="left:472px;top:676px;width:254px;font-size:14px;line-height:18.5px">
    <div class="row">DOUBLES<span class="leader"></span>$2.99</div>
    <div class="row" style="line-height:15px">GOURMET DOUBLES<span class="leader"></span>$3.99</div>
    <span class="sub" style="font-weight:700;line-height:10px">(CHICKEN, GOAT, SHRIMP)</span>
    <div class="row">ALOO PIE<span class="leader"></span>$3.99</div>
    <div class="row">SAHIENA<span class="leader"></span>$3.99</div>
    <div class="row">PHULOURIE (10)<span class="leader"></span>$3.99</div>
  </div>
  <p class="note" style="position:absolute;left:472px;top:780px;line-height:9px;font-size:8px">WITH TAMARID OR OTHER CHOICE OF SAUCE<br>WITH CHANNA ADD $.50 OR MEAT ADD $2.50</p>

  <div class="photo" role="img" aria-label="Fresh spinach leaves" style="left:746px;top:690px;width:254px;height:170px;border-radius:50% 45% 0 0;background:radial-gradient(circle at 40% 45%,#5c9a36,var(--greens) 55%,#274816)"></div>

  <!-- Vegetarian -->
  <h2 class="slab-title" style="left:832px;top:40px;width:336px;font-size:40px;letter-spacing:1px">VEGETARIAN<br>DISHES</h2>
  <div class="tag" style="left:820px;top:160px;width:162px;height:44px">VEGGIE PLATTER<small>(4 ITEMS)</small><span class="price">$13.99</span></div>
  <div class="tag" style="left:820px;top:220px;width:162px;height:44px">POTATO/CHANNA<span class="price">$9.99</span></div>
  <div class="photo" role="img" aria-label="Veggie platter with roti, pumpkin, spinach and chickpeas" style="left:988px;top:132px;width:196px;height:128px;border-radius:50%;background:radial-gradient(ellipse,#c66a2a 20%,#5a6a2a 45%,var(--plate) 66%,transparent 68%)"></div>
  <div class="photo" role="img" aria-label="Tomato" style="left:1112px;top:240px;width:120px;height:144px;border-radius:50%;background:radial-gradient(circle at 45% 40%,#f25a3c,var(--tomato) 55%,#a0170e)"></div>

  <h2 class="slab-title" style="left:824px;top:312px;font-size:22px;letter-spacing:1px;text-align:left">YOUR CHOICE OF...</h2>
  <section class="panel" style="left:840px;top:344px;width:316px;height:180px"></section>
  <div class="choice" style="left:854px;top:370px">
    <p style="margin-bottom:5px">POTATO</p>
    <p class="red">CHANNA<span class="sub">(CHICKPEAS)</span></p>
    <p style="margin-top:4px">CHANNA &amp; ALOO<span class="sub">(CHICKPEAS &amp; POTATO)</span></p>
    <p class="red" style="margin-top:4px">BHAJI<span class="sub">(SPINACH)</span></p>
    <p style="margin-top:4px">BIAGAN CHOKA<span class="sub">(EGGPLANT)</span></p>
  </div>
  <div class="choice" style="left:1010px;top:370px">
    <p>CURRY<br>MANGO</p>
    <p class="red" style="margin-top:4px">TOMATOES<br>CHOKA</p>
    <p style="margin-top:6px">PUMPKIN</p>
    <p class="red" style="margin-top:6px">FRY CABBAGE</p>
    <p style="margin-top:5px">BIAGAN &amp; ALOO<span class="sub">(EGGPLANT &amp; POTATO)</span></p>
  </div>
  <div class="photo" role="img" aria-label="Large vegetarian plate with roti, pumpkin, spinach, tomato choka and hot pepper" style="left:852px;top:510px;width:348px;height:244px;border-radius:50% 0 0 50%;background:radial-gradient(ellipse at 60% 50%,#e08a2a 18%,#4d5a22 38%,#eee8dc 55%,var(--plate) 70%,transparent 72%)"></div>

</main>
</body>
</html>
```